Software button icons

We need all of software button icons to be redesigned to give our software a very up-to-date look and feel.

Not over fussy as they currently are. Please follow the latests trends. Simple, identifiable and consistent.

I would like the colour pallet to suit our logo & website
fenlark.quodisk.com orange / blue / grey.

You can also find out lots about our software on the site to gauge to mood.

I have attached an image of the icons as they look in place now on our software and also attached the actual .bmp files the software uses to display the icons.

We will need the final artwork returned in the same size, resolution and format as the current .bmp files.

Each button is 30 pixels tall and 46 pixels wide.
The 46x30 is because room is left in the height to put the label txt.

Note:
Please ignore the yellow ? help button icon we want to remove that so the icon bars including those can be 46 pixels shorter.
There is also another FenLark icon with red writing that does
not appear on the .bmp tool-bars but is in the main image, that was used to access the about details but we are also removing it
so please ignore this.

Thanks in advance

Industry/Entity Type

Software

```html
<!DOCTYPE html>
<html lang="en">
<head>
<meta charset="utf-8">
<title>Job Editor</title>
<link href="https://fonts.googleapis.com/css2?family=Noto+Sans:wght@400;700&display=swap" rel="stylesheet">
<style>
  :root{
    --desk:#2f6fd0;
    --title-a:#c9dcf2;
    --title-b:#9fbfe6;
    --chrome:#f0f0f0;
    --line:#a0a0a0;
    --grid:#c8c8c8;
    --ink:#000;
    --muted:#6d6d6d;
    --btn-edge:#9a9a9a;
    --icon-dark:#3a3a3a;
    --icon-orange:#f07b1e;
    --icon-blue:#3b6fb6;
    --icon-blue-soft:#6f98d2;
    --white:#fff;
  }
  *{box-sizing:border-box;margin:0;padding:0}
  html,body{width:1200px;height:408px;overflow:hidden;background:var(--desk)}
  body{font-family:"Noto Sans",Tahoma,sans-serif;font-size:13px;color:var(--ink)}
  .window{position:absolute;left:0;top:0;width:1200px;height:408px;background:var(--chrome);border:1px solid #6f8fb8}
  .titlebar{height:40px;background:linear-gradient(var(--title-a),var(--title-b));display:flex;align-items:center;padding-left:8px;gap:8px}
  .app-mark{width:20px;height:20px;background:var(--icon-orange);border-radius:3px}
  .title{font-size:15px;font-weight:700;color:var(--white);text-shadow:0 0 3px #4a6a9a}
  .window-controls{margin-left:auto;display:flex;gap:4px;padding-right:10px}
  .window-controls span{width:22px;height:20px;background:var(--chrome);border:1px solid var(--btn-edge);display:flex;align-items:center;justify-content:center;font-size:12px;font-weight:700}
  .menubar{height:23px;display:flex;gap:14px;align-items:center;padding-left:14px;font-size:14px;color:var(--muted);background:var(--chrome)}
  .toolbar{height:80px;display:flex;align-items:center;padding-left:16px;border-top:1px solid var(--white);border-bottom:1px solid var(--line)}
  .tool{width:70px;height:74px;margin-right:3px;background:linear-gradient(#f6f6f6,#dcdcdc);border:1px solid var(--btn-edge);display:flex;flex-direction:column;align-items:center;justify-content:flex-end;padding-bottom:3px;font-size:13px;white-space:nowrap}
  .tool svg{width:36px;height:40px;margin-bottom:4px}
  .tool.disabled{color:#9a9a9a}
  .gap{width:8px}
  .grid-area{position:absolute;left:12px;top:146px;width:1164px;height:228px;background:#ababab;border:1px solid #7a7a7a}
  table{border-collapse:collapse;table-layout:fixed;background:var(--white);font-size:13px}
  th,td{border:1px solid var(--grid);height:25px;padding:0 3px;white-space:nowrap;overflow:hidden;text-align:left;font-weight:400}
  thead th{height:32px;background:var(--chrome);vertical-align:middle}
  td.row-head{background:var(--chrome)}
  td.num{text-align:right}
  tr.current td.name{outline:2px solid var(--ink);outline-offset:-2px}
  .hscroll{position:absolute;left:0;bottom:0;width:1145px;height:20px;background:var(--chrome);border-top:1px solid var(--grid);display:flex;justify-content:space-between;align-items:center;padding:0 4px;font-size:10px}
  .hscroll b{display:block;position:absolute;left:18px;width:1100px;height:16px;top:2px;background:#cdcdcd}
  .statusbar{position:absolute;left:0;bottom:0;width:100%;height:30px;display:flex;align-items:center;padding-left:8px;font-size:14px;border-top:1px solid var(--line)}
  .status-cells{margin-left:auto;display:flex;gap:4px;padding-right:20px}
  .status-cells span{width:54px;height:20px;border:1px solid var(--line)}
</style>
</head>
<body>
<div class="window">
  <header class="titlebar">
    <span class="app-mark"></span>
    <span class="title">Untitled - Job Editor</span>
    <div class="window-controls"><span>_</span><span>□</span><span>✕</span></div>
  </header>
  <nav class="menubar"><span>File</span><span>Edit</span><span>View</span><span>Setup</span><span>Help</span></nav>

  <div class="toolbar">
    <div class="tool"><svg viewBox="0 0 36 40"><path d="M6 2h17l8 8v28H6z" fill="var(--icon-dark)"/><path d="M23 2v8h8" fill="var(--icon-orange)"/></svg>New Job</div>
    <div class="tool"><svg viewBox="0 0 36 40"><path d="M6 2h17l8 8v28H6z" fill="var(--icon-dark)"/><path d="M23 2v8h8" fill="var(--icon-orange)"/><path d="M16 14l8 6-8 6" fill="none" stroke="#fff" stroke-width="3"/></svg>Open Job</div>
    <div class="tool"><svg viewBox="0 0 36 40"><path d="M6 2h17l8 8v28H6z" fill="var(--icon-dark)"/><path d="M23 2v8h8" fill="var(--icon-orange)"/><path d="M18 16v14M11 23h14" stroke="#fff" stroke-width="3"/></svg>Add Files</div>
    <div class="tool"><svg viewBox="0 0 36 40"><rect x="4" y="5" width="28" height="30" rx="3" fill="var(--icon-dark)"/><rect x="10" y="5" width="16" height="10" fill="var(--icon-orange)"/><rect x="9" y="22" width="18" height="10" fill="#fff"/></svg>Save Job</div>
    <div class="gap"></div>
    <div class="tool"><svg viewBox="0 0 36 40"><path d="M12 4l12 22M24 4L12 26" stroke="var(--icon-dark)" stroke-width="3"/><circle cx="11" cy="31" r="5" fill="none" stroke="var(--icon-orange)" stroke-width="3"/><circle cx="25" cy="31" r="5" fill="none" stroke="var(--icon-orange)" stroke-width="3"/></svg>Cut</div>
    <div class="tool"><svg viewBox="0 0 36 40"><path d="M12 4h13l6 6v24H12z" fill="var(--icon-orange)"/><path d="M5 10h13l6 6v22H5z" fill="var(--icon-dark)"/></svg>Copy</div>
    <div class="tool disabled"><svg viewBox="0 0 36 40"><path d="M6 2h17l8 8v28H6z" fill="var(--icon-blue)"/><rect x="11" y="14" width="14" height="18" fill="var(--icon-blue-soft)"/></svg>Paste</div>
    <div class="tool"><svg viewBox="0 0 36 40"><path d="M7 7l22 26M29 7L7 33" stroke="var(--icon-orange)" stroke-width="6"/></svg>Delete</div>
    <div class="gap"></div>
    <div class="tool disabled"><svg viewBox="0 0 36 40"><path d="M6 2h17l8 8v28H6z" fill="var(--icon-blue)"/><circle cx="20" cy="22" r="7" fill="none" stroke="var(--icon-orange)" stroke-width="3"/><path d="M25 27l6 6" stroke="var(--icon-orange)" stroke-width="3"/></svg>Rev line</div>
    <div class="tool"><svg viewBox="0 0 36 40"><path d="M6 2h17l8 8v28H6z" fill="var(--icon-blue)"/><path d="M11 16h14M11 22h14M11 28h14" stroke="#fff" stroke-width="2.5"/></svg>Properties</div>
    <div class="tool disabled"><svg viewBox="0 0 36 40"><circle cx="18" cy="20" r="12" fill="none" stroke="var(--icon-dark)" stroke-width="6" stroke-dasharray="4 3"/><circle cx="18" cy="20" r="6" fill="var(--icon-dark)"/></svg>Process</div>
    <div class="tool"><svg viewBox="0 0 36 40"><path d="M2 20Q18 6 34 20Q18 34 2 20z" fill="var(--icon-blue)"/><circle cx="18" cy="20" r="6" fill="#fff"/><circle cx="18" cy="20" r="3" fill="var(--icon-dark)"/></svg>View</div>
    <div class="tool"><svg viewBox="0 0 36 40"><rect x="10" y="4" width="16" height="10" fill="#fff" stroke="var(--icon-dark)" stroke-width="2"/><rect x="3" y="14" width="30" height="14" rx="2" fill="var(--icon-dark)"/><rect x="10" y="26" width="16" height="10" fill="#fff" stroke="var(--icon-dark)" stroke-width="2"/></svg>Output</div>
    <div class="tool"><svg viewBox="0 0 36 40"><path d="M8 8h20l6 14H2z" fill="var(--icon-dark)"/><rect x="2" y="22" width="32" height="12" fill="var(--icon-dark)"/><rect x="6" y="26" width="24" height="3" fill="var(--icon-orange)"/></svg>Scan</div>
  </div>

  <div class="grid-area">
    <table>
      <colgroup>
        <col style="width:47px"><col style="width:480px"><col style="width:29px"><col style="width:44px"><col style="width:32px"><col style="width:146px"><col style="width:44px"><col style="width:105px"><col style="width:114px"><col style="width:102px">
      </colgroup>
      <thead><tr><th></th><th>Filename</th><th>Ext</th><th>Status</th><th>Qty</th><th>Size</th><th>Media</th><th>Output</th><th>Pens</th><th>Format</th></tr></thead>
      <tbody>
        <tr><td class="row-head">Proto</td><td></td><td></td><td></td><td class="num">1</td><td>Auto Detected</td><td>Bond</td><td>100%</td><td>User Specified</td><td>User Specified</td></tr>
        <tr><td class="row-head">1</td><td class="name">1344465690 - Copy - Copy</td><td>pdf</td><td></td><td class="num">1</td><td>User-Specified &nbsp;(1066</td><td>Bond</td><td>User-Specified</td><td>User Specified</td><td>PDF</td></tr>
        <tr><td class="row-head">2</td><td class="name">1344465690 - Copy (2) - Copy</td><td>pdf</td><td></td><td class="num">1</td><td>User-Specified &nbsp;(1066</td><td>Bond</td><td>User-Specified</td><td>User Specified</td><td>PDF</td></tr>
        <tr class="current"><td class="row-head">3</td><td class="name">1344465690 - Copy (2)</td><td>pdf</td><td></td><td class="num">1</td><td>User-Specified &nbsp;(1066</td><td>Bond</td><td>User-Specified</td><td>User Specified</td><td>PDF</td></tr>
        <tr><td class="row-head">4</td><td class="name">1344465690 - Copy (3) - Copy</td><td>pdf</td><td></td><td class="num">1</td><td>User-Specified &nbsp;(1066</td><td>Bond</td><td>User-Specified</td><td>User Specified</td><td>PDF</td></tr>
        <tr><td class="row-head">5</td><td class="name">1344465690 - Copy - Copy (4)</td><td>pdf</td><td></td><td class="num">1</td><td>User-Specified &nbsp;(1066</td><td>Bond</td><td>User-Specified</td><td>User Specified</td><td>PDF</td></tr>
      </tbody>
    </table>
    <div class="hscroll"><span>◀</span><b></b><span>▶</span></div>
  </div>

  <footer class="statusbar">For Help, press F1<div class="status-cells"><span></span><span></span><span></span></div></footer>
</div>
</body>
</html>
```